Stationery Design Project

Would like to have the design elements we created in for our website (www.brook-holdings.example), incorporated in a stationery design layout.
Updates
Colors used in the logo attachments do not need to be used. We are open to different color variations. Looking for a crisp, clean, modern update using the design elements in attachments and which can also be viewed on or website.
A note to designers:
Project Deadline Extended
Reason: Due to update in our project description and requirements, we have decided to extend the deadline of this project to provide ample opportunity to all designers participating .
Requirements
Must have
- Must have continuity with the theme and design features used in our website. Have attached .jpg images of some of the design elements.

```html
<!DOCTYPE html>
<html lang="en">
<head>
<meta charset="utf-8">
<title>Brook Holdings Letterhead</title>
<link href="https://fonts.googleapis.com/css2?family=Arimo:wght@400;700&display=swap" rel="stylesheet">
<style>
  :root {
    --backdrop: #5b5a57;
    --paper: #ffffff;
    --ink: #1f1f1f;
    --muted: #6d6d6d;
    --brand-blue: #2b86c5;
    --mark-blue: #6aa6d8;
    --meadow-dark: #7da94a;
    --meadow-mid: #a9c75a;
    --meadow-light: #e6df62;
  }
  * { box-sizing: border-box; margin: 0; padding: 0; }
  html, body {
    width: 1200px; height: 849px; overflow: hidden;
    background: var(--backdrop);
  }
  .letterhead {
    position: absolute; left: 303px; top: 40px;
    width: 594px; height: 770px;
    background: var(--paper);
    font-family: "Arimo", Arial, sans-serif;
    color: var(--ink);
    font-size: 12.3px; line-height: 14px;
  }
  .brand-mark {
    position: absolute; left: 0; right: 0; top: 62px;
    text-align: center;
    font-size: 40px; line-height: 44px; font-weight: 400;
    color: var(--mark-blue);
  }
  .letter-body { position: absolute; left: 38px; width: 518px; }
  .letter-date { top: 162px; }
  .recipient { top: 203px; }
  .letter-text { top: 301px; hyphens: auto; }
  .letter-text p { text-align: justify; margin-bottom: 14px; }
  .letter-text .salutation { margin-bottom: 0; }
  .closing { top: 497px; }
  .signatory { top: 567px; }
  .footer-brand {
    position: absolute; left: 38px; top: 658px;
    font-size: 24px; line-height: 28px; font-weight: 400;
    color: var(--brand-blue);
  }
  .footer-contact {
    position: absolute; left: 38px; top: 692px;
    font-size: 7.2px; line-height: 10px; color: var(--muted);
  }
  .footer-contact .label { color: var(--brand-blue); }
  .footer-contact .web { color: var(--brand-blue); font-weight: 700; }
  .meadow-band {
    position: absolute; left: 0; right: 0; bottom: 0; height: 38px;
    background: linear-gradient(90deg, var(--meadow-dark) 0%, var(--meadow-mid) 45%, var(--meadow-mid) 70%, var(--meadow-light) 100%);
  }
</style>
</head>
<body>
  <main class="letterhead">
    <div class="brand-mark">Brook</div>

    <div class="letter-body letter-date">September 10, 2012</div>

    <address class="letter-body recipient" style="font-style:normal">
      Ms. Carol Whitfield<br>
      Accounts Payable<br>
      The Kettle Shop<br>
      482 Linden Court<br>
      Harbor View, CA 90210
    </address>

    <div class="letter-body letter-text">
      <p class="salutation">Dear Ms. Whitfield,</p>
      <p>It has come to my attention that your company, The Kettle Shop has been late with paying their invoices for the past three months.</p>
      <p>In order to encourage our customers to pay for their invoices before the due date, we have implemented a discount model where we'll give you 2% off your invoice if you pay us within 10 days of receiving the invoice.</p>
      <p>I hope that everything is going well for you and your company. You are one of our biggest customers, and we appreciate your business. If you have any questions, feel free to contact me at (555) 010-2233.</p>
    </div>

    <div class="letter-body closing">Sincerely,</div>

    <div class="letter-body signatory">
      Dan Mercer<br>
      Accounts Receivable
    </div>

    <div class="footer-brand">Brook Holdings</div>
    <div class="footer-contact">
      118 Millrace Road Suite 40. Fairbrook, GA 30599<br>
      <span class="label">Phone</span> : (706) 555-0142 &nbsp;|&nbsp; <span class="label">Fax</span> : (706) 555-0199 &nbsp;|&nbsp; <span class="label">E-mail</span> : info@brook-holdings.example<br>
      <span class="web">www.brook-holdings.example</span>
    </div>

    <div class="meadow-band" role="img" aria-label="Soft-focus photograph of green meadow grass fading to yellow light"></div>
  </main>
</body>
</html>
```